Design CD-Velvet Tadpole/WAIT FOR THE ORANGE TRAIN
Zielgruppe
Wir sind Velvet Tadpole eine INDIE/ALTERNATIVE Band.. bestehend aus 4 Jungs im alter von durchschnittlich 22 Jahren. Wir suchen ein Design für unsere 2. Platte die den Namen 'WAIT FOR THE ORANGE TRAIN' trägt. Im gleichnamigen Song geht es um einen Menschen der am Limit lebt und jeden Moment ohne Rücksicht auf andere auskostet.. als er eines Tages versteht wie er den Menschen die er liebt damit Schaden zufügt, verspricht er seiner LIEBE:'I SWEAR I WILL WAIT FOR THE ORANGE TRAIN'..'im nächsten Leben werde ich ein besserer Typ sein.
Unsere Musik zeichnet sich durch 3 Stimmigen Gesang, verspielte teilweise psychodelische Sounds und eingängige Melodien die sich zu unserem Markenzeichen entwickelt haben aus.
Aufgabenstellung
Das Design soll Modern,verspielt,Bunt, gerne etwas abstrakt und vor allem Grafisch (nicht im realistic style) sein.
Beispielbilder in welche Richtung es gehen soll lege ich in den Anhang.

```html
<!DOCTYPE html>
<html lang="en">
<head>
<meta charset="utf-8">
<title>Velvet Tadpole – Wait for the Orange Train</title>
<link href="https://fonts.googleapis.com/css2?family=Syncopate:wght@700&display=swap" rel="stylesheet">
<style>
  :root {
    --stage-dark: #050505;
    --stage-mid: #1c1c1c;
    --ink: #0d171c;
    --marble-white: #f6f9f9;
    --marble-ice: #cde5ea;
    --marble-teal: #3d9fb2;
    --marble-aqua: #7cc6d2;
    --marble-deep: #1a5666;
    --marble-grey: #8e9ea3;
    --marble-umber: #8d6a48;
    --line-light: rgba(255, 255, 255, 0.75);
    --line-dark: rgba(20, 60, 72, 0.55);
  }
  html, body {
    margin: 0;
    padding: 0;
    width: 1200px;
    height: 683px;
    overflow: hidden;
  }
  body {
    background: radial-gradient(ellipse at 50% 45%, var(--stage-mid) 0%, var(--stage-dark) 75%);
    font-family: "Syncopate", "Arial Black", sans-serif;
  }
  .album-cover {
    position: absolute;
    left: 290px;
    top: 31px;
    width: 620px;
    height: 620px;
    overflow: hidden;
    box-shadow: 0 0 14px rgba(255, 255, 255, 0.3);
    background: var(--marble-white);
  }
  .cover-artwork {
    position: absolute;
    inset: 0;
    width: 100%;
    height: 100%;
  }
  .cover-lines {
    position: absolute;
    inset: 0;
    width: 100%;
    height: 100%;
    pointer-events: none;
  }
  .band-name,
  .album-title {
    position: absolute;
    margin: 0;
    color: var(--ink);
    font-weight: 700;
    text-transform: uppercase;
    white-space: nowrap;
    line-height: 1;
  }
  .band-name {
    top: 58px;
    left: 0;
    width: 100%;
    padding-right: 36px;
    box-sizing: border-box;
    text-align: center;
    font-size: 24px;
    letter-spacing: 6px;
    word-spacing: 16px;
  }
  .album-title {
    bottom: 28px;
    left: 22px;
    right: 18px;
    display: flex;
    justify-content: space-between;
    font-size: 19px;
    letter-spacing: 3px;
  }
</style>
</head>
<body>
  <main class="album-cover">
    <svg class="cover-artwork" viewBox="0 0 620 620" preserveAspectRatio="none" role="img" aria-label="Marbled artwork in teal, white, grey and umber with a hooded figure seen from behind, a faint city skyline and geometric triangle fragments">
      <defs>
        <linearGradient id="marble-base" x1="0" y1="0" x2="1" y2="1">
          <stop offset="0" stop-color="#b9cfd3"/>
          <stop offset="0.22" stop-color="#f6f9f9"/>
          <stop offset="0.45" stop-color="#cde5ea"/>
          <stop offset="0.62" stop-color="#f6f9f9"/>
          <stop offset="0.82" stop-color="#7cc6d2"/>
          <stop offset="1" stop-color="#3d9fb2"/>
        </linearGradient>
        <radialGradient id="figure-tone" cx="0.5" cy="0.55" r="0.5">
          <stop offset="0" stop-color="#8d6a48"/>
          <stop offset="0.35" stop-color="#1a5666"/>
          <stop offset="0.75" stop-color="#3d9fb2" stop-opacity="0.6"/>
          <stop offset="1" stop-color="#cde5ea" stop-opacity="0"/>
        </radialGradient>
        <linearGradient id="ground-tone" x1="0" y1="0" x2="0" y2="1">
          <stop offset="0" stop-color="#3d9fb2" stop-opacity="0"/>
          <stop offset="1" stop-color="#1a5666" stop-opacity="0.75"/>
        </linearGradient>
      </defs>
      <rect width="620" height="620" fill="url(#marble-base)"/>
      <rect x="110" y="130" width="360" height="460" fill="url(#figure-tone)"/>
      <rect x="0" y="430" width="620" height="190" fill="url(#ground-tone)"/>
    </svg>

    <svg class="cover-lines" viewBox="0 0 620 620" aria-hidden="true">
      <g stroke="var(--line-dark)" stroke-width="1.5" fill="none">
        <line x1="24" y1="150" x2="24" y2="440"/>
        <line x1="40" y1="120" x2="40" y2="310"/>
        <line x1="76" y1="330" x2="76" y2="470"/>
        <line x1="96" y1="390" x2="96" y2="520"/>
      </g>
      <g stroke="var(--line-light)" stroke-width="1" fill="none">
        <line x1="0" y1="90" x2="200" y2="0"/>
        <line x1="380" y1="620" x2="620" y2="330"/>
        <line x1="150" y1="190" x2="60" y2="480"/>
        <polyline points="30,230 150,150 150,430"/>
        <line x1="0" y1="478" x2="620" y2="478"/>
      </g>
    </svg>

    <h1 class="band-name">Velvet Tadpole</h1>
    <h2 class="album-title">
      <span>Wait</span><span>For</span><span>The</span><span>Orange</span><span>Train</span>
    </h2>
  </main>
</body>
</html>
```